Business Card Design

We need a business card designed to portray the message that we are wedding and event stylists. We set up garden ceremonies and style wedding reception venues with chair covers and sashes, backdrops and draping's, wishing wells, tealight holders, table centerpieces. We also style corporate functions - Christmas parties, gala dinners, school formals, award nights. The colour of our uniforms are black and hot pink, if these colours could be incorporated. We would like to be able to use this design for letterhead, flyers and postcards etc. We would like the design to portray a professional, classic image that would relate to both spectrums of our business, weddings and corporate events. If you could develop a logo to incorporate would be great

Target Market(s)

brides, corporate compaines

Industry/Entity Type

Wedding

Contact Information for Business Card

Velvet Aisle & Function Rentals
Phone: 0413 586 190 Email:vaafr@quokkamail.com
Web: www.velvetaisleandfunctions.com.au

Requirements
Must have
• Must include that we set up for weddings, engagements, birthdays, anniversaries, corporate functions, school formals, any occasion.

```html
<!DOCTYPE html>
<html lang="en">
<head>
<meta charset="utf-8">
<title>Velvet Aisle &amp; Function Rentals — Business Card</title>
<link rel="stylesheet" href="https://fonts.googleapis.com/css2?family=Pinyon+Script&family=Cinzel:wght@400;600&display=swap">
<style>
  :root {
    --mist-light: #dfe6df;
    --mist-mid: #b9c9c3;
    --sage-deep: #7f958f;
    --dew-blue: #93aebf;
    --ink: #111314;
    --hot-pink: #e21fd6;
    --white: #ffffff;
  }
  html, body {
    margin: 0;
    padding: 0;
    width: 1200px;
    height: 741px;
    overflow: hidden;
    background: var(--white);
  }
  .card {
    position: relative;
    width: 1200px;
    height: 741px;
    overflow: hidden;
    font-family: "Cinzel", "Times New Roman", serif;
  }
  .card__photo {
    position: absolute;
    inset: 0;
    background:
      radial-gradient(ellipse 45% 40% at 48% 42%, rgba(240,244,238,0.85), rgba(240,244,238,0) 70%),
      radial-gradient(ellipse 30% 30% at 8% 52%, rgba(95,112,106,0.55), rgba(95,112,106,0) 70%),
      radial-gradient(ellipse 25% 30% at 95% 50%, rgba(110,128,124,0.5), rgba(110,128,124,0) 70%),
      radial-gradient(ellipse 60% 35% at 50% 100%, rgba(130,160,180,0.75), rgba(130,160,180,0) 75%),
      linear-gradient(180deg, var(--mist-light) 0%, var(--mist-mid) 45%, var(--dew-blue) 100%);
  }
  .card__name {
    position: absolute;
    left: 0;
    right: 0;
    top: 52px;
    margin: 0;
    text-align: center;
    font-family: "Pinyon Script", cursive;
    font-weight: 400;
    color: var(--white);
    line-height: 1;
  }
  .card__name-line {
    display: block;
    font-size: 108px;
  }
  .card__name-join {
    display: block;
    font-size: 64px;
    margin: -22px 0 -26px;
  }
  .card__contact {
    position: absolute;
    left: 0;
    right: 0;
    top: 362px;
    margin: 0;
    text-align: center;
    color: var(--ink);
    font-size: 22px;
    letter-spacing: 2.2px;
    line-height: 38px;
  }
  .card__contact-line { display: block; }
  .card__phone {
    color: var(--hot-pink);
    font-family: Arial, Helvetica, sans-serif;
    font-weight: 700;
    letter-spacing: 1.5px;
  }
  .card__services {
    position: absolute;
    left: 0;
    right: 0;
    top: 550px;
    margin: 0;
    text-align: center;
    color: var(--white);
    font-size: 22px;
    letter-spacing: 2.4px;
    line-height: 41px;
  }
  .card__services-line { display: block; }
</style>
</head>
<body>
  <main class="card">
    <div class="card__photo" role="img" aria-label="Soft-focus close-up of dew drops on pale grass and seed heads in misty sage and blue tones"></div>

    <h1 class="card__name">
      <span class="card__name-line">Velvet Aisle</span>
      <span class="card__name-join">and</span>
      <span class="card__name-line">Function Rentals</span>
    </h1>

    <p class="card__contact">
      <span class="card__contact-line">Phone: <span class="card__phone">0413 586 190</span> | Email: vaafr@quokkamail.com</span>
      <span class="card__contact-line">www.velvetaisleandfunctions.com.au</span>
    </p>

    <p class="card__services">
      <span class="card__services-line">We arrange for weddings | engagements</span>
      <span class="card__services-line">birthdays | anniversaries</span>
      <span class="card__services-line">corporate functions | school formals | any occasion</span>
    </p>
  </main>
</body>
</html>
```